Complete Website Redesign

We need a complete revamp of our website. Need to add interactive custmer catalog seection tools. Need to add customer spec input for recommended product search results. Need a cutomer lead and opportunity contact capability. Need a complete Branding message revamp. Primary visuals will be prodcut pictures and case studies.
Target Market(s)
Industrial Customers in the high durability Air movement and fan/blower space; high durability enclosure and flow industries ie. mining, chamicals, manufacturing, water treatment, chemical in use manufacturing
Look and feel

```html
<!DOCTYPE html>
<html lang="en">
<head>
<meta charset="utf-8">
<title>Duraflow Composites, LLC</title>
<link href="https://fonts.googleapis.com/css2?family=PT+Sans:wght@400;700&family=PT+Sans+Narrow&display=swap" rel="stylesheet">
<style>
  :root {
    --brand: #2c3aa0;
    --brand-soft: #3a48a8;
    --band: #6370bf;
    --nav-top: #7a86d2;
    --nav-bottom: #4b58b4;
    --button: #1c2b8a;
    --text: #555a66;
    --muted: #7076b8;
    --line: #d8dbe6;
    --footer-top: #5b66b0;
    --footer-bottom: #2e3a8a;
    --white: #ffffff;
  }
  * { box-sizing: border-box; margin: 0; padding: 0; }
  html, body { width: 1087px; height: 1200px; overflow: hidden; }
  body { position: relative; background: var(--white); font-family: "PT Sans", sans-serif; color: var(--text); }
  .abs { position: absolute; }

  .top-rule { left: 0; top: 0; width: 1087px; height: 6px; background: #eeeeee; }
  .brand { left: 80px; top: 52px; display: flex; align-items: center; gap: 12px; }
  .brand-mark { width: 34px; height: 34px; background: var(--brand); }
  .brand-name { font-size: 21px; font-weight: 700; color: var(--brand); }

  .social { right: 84px; top: 29px; display: flex; gap: 6px; }
  .social span { width: 20px; height: 20px; background: #4a6cc0; display: block; border-radius: 2px; }
  .phone { right: 84px; top: 56px; font-size: 22px; color: #444; display: flex; align-items: center; gap: 6px; }
  .email { right: 84px; top: 83px; font-size: 13.5px; color: #555; display: flex; align-items: center; gap: 6px; }

  .nav { left: 80px; top: 113px; width: 934px; height: 47px; display: flex; background: linear-gradient(var(--nav-top), var(--nav-bottom)); }
  .nav a { font-family: "PT Sans Narrow", sans-serif; font-size: 17px; color: var(--white); text-decoration: none; display: flex; align-items: center; justify-content: center; border-right: 1px solid rgba(255,255,255,.25); }
  .nav a:last-child { border-right: none; }

  .hero-bg { left: 0; top: 160px; width: 1087px; height: 369px; background: linear-gradient(#f3f3f5, #ffffff 60%, #f6f6f8); border-top: 1px solid #e2e2e6; border-bottom: 1px solid #dedee4; }
  .hero-kicker { left: 87px; top: 250px; font-size: 27px; color: #444; font-weight: 400; }
  .hero-title { left: 87px; top: 286px; font-size: 35px; color: var(--brand); font-weight: 700; }
  .hero-copy { left: 87px; top: 336px; width: 420px; font-size: 13.5px; line-height: 21px; color: #555; }
  .dots { left: 88px; top: 389px; display: flex; gap: 3px; }
  .dots span { width: 13px; height: 13px; border-radius: 50%; background: #cfd3ee; display: block; }
  .dots span:first-child { background: var(--band); }
  .hero-visual { left: 634px; top: 179px; width: 287px; height: 313px; background: radial-gradient(circle at 45% 45%, #f4f4f6, #c9cbd2 75%); border-radius: 40% 30% 6px 6px; }

  .products { left: 73px; top: 491px; width: 942px; height: 284px; background: var(--band); }
  .card { top: 503px; width: 216px; height: 255px; background: linear-gradient(#ffffff 60%, #eef0fa); border: 1px solid #c9cdee; text-align: center; }
  .card-visual { width: 76px; height: 88px; margin: 16px auto 12px; background: radial-gradient(circle, #c4c7d0, #eceef3 70%); }
  .card h3 { font-size: 18px; font-weight: 400; color: var(--brand-soft); line-height: 23px; padding: 0 14px; }
  .card p { font-size: 11.5px; line-height: 16.5px; color: var(--muted); padding: 4px 18px 0; height: 50px; }
  .card .btn { position: absolute; left: 65px; top: 210px; width: 86px; height: 24px; background: var(--button); color: var(--white); font-size: 12px; line-height: 24px; border-radius: 2px; }

  .welcome { left: 84px; top: 808px; width: 620px; }
  .welcome h1 { font-size: 25px; font-weight: 400; color: #222; margin-bottom: 8px; }
  .welcome p { font-size: 12.5px; line-height: 23px; color: #666; margin-bottom: 7px; }

  .services { left: 732px; top: 804px; width: 279px; height: 243px; border: 1px solid var(--line); }
  .services h2 { height: 47px; background: linear-gradient(#fafafa, #e6e6e8); border-bottom: 1px solid #cfcfd4; font-size: 20px; font-weight: 400; color: #333; padding: 12px 0 0 25px; }
  .services ul { list-style: none; padding: 17px 0 0 29px; }
  .services li { font-size: 12.5px; color: #555; height: 24.6px; display: flex; align-items: center; gap: 10px; }

  .footer { left: 0; top: 1103px; width: 1087px; height: 97px; background: linear-gradient(var(--footer-top), var(--footer-bottom)); }
  .copyright { left: 85px; top: 1133px; font-size: 12px; color: #d4d8f0; }
  .footer-links { right: 82px; top: 1132px; font-family: "PT Sans Narrow", sans-serif; font-size: 13.5px; color: var(--white); }
  .footer-links span { margin: 0 5px; }
</style>
</head>
<body>
  <div class="abs top-rule"></div>

  <div class="abs brand">
    <span class="brand-mark"></span>
    <span class="brand-name">Duraflow Composites, LLC</span>
  </div>

  <div class="abs social"><span></span><span></span><span></span></div>
  <div class="abs phone">
    <svg width="18" height="18" viewBox="0 0 24 24"><path d="M6.6 10.8c1.4 2.8 3.8 5.1 6.6 6.6l2.2-2.2c.3-.3.7-.4 1-.2 1.1.4 2.3.6 3.6.6.6 0 1 .4 1 1V20c0 .6-.4 1-1 1C10.6 21 3 13.4 3 4c0-.6.4-1 1-1h3.5c.6 0 1 .4 1 1 0 1.3.2 2.5.6 3.6.1.3 0 .7-.2 1z" fill="#9a9ca4"/></svg>
    555-014-2290
  </div>
  <div class="abs email">
    <svg width="16" height="11" viewBox="0 0 16 11"><rect x=".5" y=".5" width="15" height="10" fill="none" stroke="#9a9ca4"/><path d="M.5.5 8 6l7.5-5.5" fill="none" stroke="#9a9ca4"/></svg>
    sales@duraflowco.com
  </div>

  <nav class="abs nav">
    <a href="#" style="width:114px">HOME</a>
    <a href="#" style="width:148px">PRODUCTS</a>
    <a href="#" style="width:144px">ABOUT US</a>
    <a href="#" style="width:131px">MISSION</a>
    <a href="#" style="width:243px">REQUEST INFORMATION</a>
    <a href="#" style="width:154px">CONTACTS</a>
  </nav>

  <div class="abs hero-bg"></div>
  <div class="abs hero-kicker">Provide Wide selection of fiberglass</div>
  <div class="abs hero-title">Plant Maintenance Operations</div>
  <p class="abs hero-copy">Mauris vel lacus vitae felis vestibulum volutpat. Etiam est nunc, venenatis in, tristique eu, imperdiet ac, nisl.</p>
  <div class="abs dots"><span></span><span></span><span></span><span></span></div>
  <div class="abs hero-visual" role="img" aria-label="Photo of a white industrial centrifugal blower with belt drive and blue motor"></div>

  <div class="abs products"></div>
  <div class="abs card" style="left:86px">
    <div class="card-visual" role="img" aria-label="Photo of a fiberglass axial propeller"></div>
    <h3>Fiberglass Axial Propellers</h3>
    <p>Phasellus felis dolor, scelerisque a, tempus eget, lobortis id, libero</p>
    <span class="btn">Learn More</span>
  </div>
  <div class="abs card" style="left:318px">
    <div class="card-visual" role="img" aria-label="Photo of a fiberglass axial fan"></div>
    <h3>Fiberglass Axial Fans</h3>
    <p>Phasellus felis dolor, scelerisque a, tempus eget, lobortis id libero Donec scelerisque</p>
    <span class="btn">Learn More</span>
  </div>
  <div class="abs card" style="left:551px">
    <div class="card-visual" role="img" aria-label="Photo of a fiberglass centrifugal fan"></div>
    <h3>Fiberglass Centrifugal Fans</h3>
    <p>Phasellus felis dolor, scelerisque a, tempus eget, lobortis id, libero</p>
    <span class="btn">Learn More</span>
  </div>
  <div class="abs card" style="left:783px">
    <div class="card-visual" role="img" aria-label="Photo of a fiberglass louver and damper unit"></div>
    <h3>Fiberglass Louvers and Dampers</h3>
    <p>Phasellus felis dolor, scelerisque a, tempus eget, lobortis id, libero</p>
    <span class="btn">Learn More</span>
  </div>

  <section class="abs welcome">
    <h1>Welcome to Duraflow Composites, LLC</h1>
    <p>Vivamus porttitor, g, purus nisi eleifend libero, a tempus libero lectus feugiat felis. Morbi diam mauris, viverra in, gravida eu, mattis in, ante. Morbi eget arcu. Morbi porta, libero id ullamcorper nonummy, nibh ligula pulvinar metus, eget consectetuer augue nisi quis lacus. Ut ac mi quis lacus mollis aliquam. Curabitur iaculis tempus eros. Curabitur vel mi sit amet magna malesuada ultrices. Ut nisi erat, fermentum vel, congue id, euismod in, elit. Fusce ultricies, orci ac feugiat suscipit, leo massa sodales velit, et scelerisque mi tortor at ipsum.</p>
    <p>Phasellus felis dolor, scelerisque a, tempus eget, lobortis id, libero. Donec scelerisque leo ac risus. Praesent sit amet est. In dictum, dolor eu dictum porttitor, enim felis viverra mi, eget luctus massa purus quis odio. Etiam nulla massa, pharetra facilisis, volutpat in, imperdiet sit amet, sem.</p>
  </section>

  <aside class="abs services">
    <h2>Services Provide</h2>
    <ul>
      <li><svg width="6" height="10"><path d="M0 0l6 5-6 5z" fill="#b0b2ba"/></svg>Class aptent taciti sociosqu</li>
      <li><svg width="6" height="10"><path d="M0 0l6 5-6 5z" fill="#b0b2ba"/></svg>Ad litora torquent per conubia</li>
      <li><svg width="6" height="10"><path d="M0 0l6 5-6 5z" fill="#b0b2ba"/></svg>Nostra per inceptos hymenaeos</li>
      <li><svg width="6" height="10"><path d="M0 0l6 5-6 5z" fill="#b0b2ba"/></svg>Proin nulla arcu nonummy</li>
      <li><svg width="6" height="10"><path d="M0 0l6 5-6 5z" fill="#b0b2ba"/></svg>Luctus dictum eget fermentum lorem</li>
      <li><svg width="6" height="10"><path d="M0 0l6 5-6 5z" fill="#b0b2ba"/></svg>Nunc porta convallis pede</li>
    </ul>
  </aside>

  <footer class="abs footer"></footer>
  <div class="abs copyright">Copyright © 2013 Company Name.&nbsp; All right reserved</div>
  <div class="abs footer-links">HOME<span>|</span>PRODUCTS<span>|</span>ABOUT US<span>|</span>MISSION<span>|</span>REQUEST INFORMATION<span>|</span>CONTACTS</div>
</body>
</html>
```